Brightmoor Partners Branding Revamp

We are a consulting company, looking for a way to display and promote our brand. We have 2 sides to the business- Brightmoor (financial) and Partners (cyber security). The financial side products relate to business necessities: card processing, website design/hosting/maintenance, VoIP phone systems. The cyber security side promotes a bundled package of 4 solutions: network vulnerability scan, dark web scan, anti-ransomeware/malware software, and image-level backups. We want people to understand that partnering with Brightmoor Partners gives them “Elevated Peace of Mind” (tagline). Current badge and logos uploaded.

Target Market(s)

Small businesses

Contact Information for Business Card

Lena Marwick, Vice President, lena@brightmoorpartners.example, 555-806-1937, www.brightmoorpartners.example

Requirements
Nice to have
• I do prefer the darker background for front and back

```html
<!DOCTYPE html>
<html lang="en">
<head>
<meta charset="utf-8">
<title>Brightmoor Partners – Business Card</title>
<link rel="stylesheet" href="https://fonts.googleapis.com/css2?family=Lato:wght@400;700&family=Michroma&display=swap">
<style>
  :root {
    --page: #ffffff;
    --card: #1c1c1e;
    --red: #d6312f;
    --red-deep: #8e2528;
    --white: #ffffff;
  }
  * { margin: 0; padding: 0; box-sizing: border-box; }
  html, body {
    width: 1200px;
    height: 1200px;
    overflow: hidden;
    background: var(--page);
  }
  .card {
    position: absolute;
    left: 147px;
    width: 913px;
    height: 513px;
    background: var(--card);
    overflow: hidden;
  }
  .card--front { top: 74px; }
  .card--back { top: 620px; }

  /* Front */
  .brand-dot {
    position: absolute;
    left: 300px;
    top: 150px;
    width: 84px;
    height: 84px;
    border-radius: 50%;
    background: var(--red);
  }
  .brand-name {
    position: absolute;
    left: 92px;
    width: 500px;
    text-align: center;
    font-family: "Michroma", sans-serif;
    font-weight: 400;
    line-height: 1;
  }
  .brand-name__main {
    top: 312px;
    font-size: 31px;
    letter-spacing: 9px;
    color: var(--white);
    -webkit-text-stroke: 1px var(--white);
  }
  .brand-name__sub {
    top: 366px;
    font-size: 15px;
    letter-spacing: 4px;
    color: var(--red);
    -webkit-text-stroke: 0.6px var(--red);
  }
  .brand-decor {
    position: absolute;
    top: 0;
    height: 100%;
    width: 225px;
  }
  .brand-decor--front { right: 0; }
  .brand-decor--back { left: 0; }

  /* Back */
  .person-name {
    position: absolute;
    left: 329px;
    top: 118px;
    font-family: "Lato", sans-serif;
    font-weight: 700;
    font-size: 44px;
    color: var(--red);
    line-height: 1.1;
  }
  .contact-list {
    position: absolute;
    left: 326px;
    top: 196px;
    list-style: none;
  }
  .contact-item {
    display: flex;
    align-items: center;
    height: 52px;
    font-family: "Lato", sans-serif;
    font-weight: 400;
    font-size: 30px;
    color: var(--white);
    white-space: nowrap;
  }
  .contact-icon {
    width: 34px;
    height: 34px;
    margin-right: 26px;
    flex: none;
  }
  .contact-dot {
    width: 28px;
    height: 28px;
    margin: 0 29px 0 3px;
    border-radius: 50%;
    background: var(--red);
    flex: none;
  }
</style>
</head>
<body>

<section class="card card--front" aria-label="Card front">
  <div class="brand-dot"></div>
  <p class="brand-name brand-name__main">BRIGHTMOOR</p>
  <p class="brand-name brand-name__sub">PARTNERS</p>
  <svg class="brand-decor brand-decor--front" role="img" aria-label="Large red brand decoration" viewBox="0 0 225 513" preserveAspectRatio="none">
    <defs>
      <linearGradient id="decorFront" x1="0" y1="0" x2="1" y2="1">
        <stop offset="0" stop-color="#d6312f"/>
        <stop offset="0.5" stop-color="#8e2528"/>
        <stop offset="1" stop-color="#d6312f"/>
      </linearGradient>
    </defs>
    <rect width="225" height="513" fill="url(#decorFront)" opacity="0.85"/>
  </svg>
</section>

<section class="card card--back" aria-label="Card back">
  <svg class="brand-decor brand-decor--back" role="img" aria-label="Large red brand decoration" viewBox="0 0 225 513" preserveAspectRatio="none">
    <defs>
      <linearGradient id="decorBack" x1="1" y1="0" x2="0" y2="1">
        <stop offset="0" stop-color="#d6312f"/>
        <stop offset="0.5" stop-color="#8e2528"/>
        <stop offset="1" stop-color="#d6312f"/>
      </linearGradient>
    </defs>
    <rect width="225" height="513" fill="url(#decorBack)" opacity="0.85"/>
  </svg>

  <h1 class="person-name">Lena Marwick</h1>
  <ul class="contact-list">
    <li class="contact-item">
      <svg class="contact-icon" viewBox="0 0 34 34" aria-hidden="true">
        <rect x="8" y="2" width="18" height="30" rx="4" fill="none" stroke="#d6312f" stroke-width="3"/>
        <circle cx="17" cy="26" r="2" fill="#d6312f"/>
      </svg>
      <span>555-806-1937</span>
    </li>
    <li class="contact-item">
      <svg class="contact-icon" viewBox="0 0 34 34" aria-hidden="true">
        <rect x="1" y="7" width="32" height="21" fill="#d6312f"/>
        <path d="M1 7 L17 19 L33 7 M1 28 L13 16 M33 28 L21 16" fill="none" stroke="#1c1c1e" stroke-width="2"/>
      </svg>
      <span>lena@brightmoorpartners.example</span>
    </li>
    <li class="contact-item">
      <span class="contact-dot"></span>
      <span>www.brightmoorpartners.example</span>
    </li>
    <li class="contact-item">
      <span class="contact-dot"></span>
      <span>brightmoor</span>
    </li>
  </ul>
</section>

</body>
</html>
```